Bref créative
Business Cards/Letterhead for a Private Equity Real Estate Company
KTR Commercial
Simple
H. Dalton Greave
President
4780 Brambling Road
Suite 610
Atlanta, GA 30342
dalton@ktrcommercial.net
http://ktrcommercial.net/
We think we want the logo on one side and then all the written information on the other. Open to seeing different suggestions, though. Thanks for everyone who participates!

```html
<!DOCTYPE html>
<html lang="en">
<head>
<meta charset="utf-8">
<title>KTR Commercial Business Card</title>
<link rel="stylesheet" href="https://fonts.googleapis.com/css2?family=Open+Sans:wght@400;600;700&display=swap">
<style>
  :root {
    --bg: #d9d9d9;
    --card: #ffffff;
    --ink: #3a3a3a;
    --muted: #6b6b6b;
    --red: #d0262d;
    --slate: #5f5f5f;
    --slate-light: #8a8a8a;
  }
  * { margin: 0; padding: 0; box-sizing: border-box; }
  html, body { width: 1200px; height: 984px; overflow: hidden; }
  body {
    background: var(--bg);
    font-family: "Open Sans", sans-serif;
    color: var(--ink);
    position: relative;
  }
  .card {
    position: absolute;
    left: 250px;
    width: 700px;
    height: 400px;
    background: var(--card);
    border-radius: 28px;
    overflow: hidden;
    box-shadow: 0 10px 30px rgba(0,0,0,0.18);
  }
  .card-front { top: 52px; }
  .card-back { top: 532px; }

  .brand { display: flex; flex-direction: column; align-items: center; }
  .brand-row { display: flex; align-items: center; gap: 12px; }
  .brand-mark { width: 22px; height: 22px; background: var(--slate); }
  .brand-name {
    font-weight: 700;
    color: var(--slate);
    letter-spacing: 2px;
    text-transform: uppercase;
  }
  .brand-tagline {
    margin-top: 6px;
    font-size: 10px;
    letter-spacing: 2px;
    color: var(--muted);
    text-transform: uppercase;
  }
  .card-front .brand {
    position: absolute; left: 0; right: 0; top: 168px;
  }
  .card-front .brand-name { font-size: 34px; }

  .card-back .brand {
    position: absolute; left: 44px; top: 36px; align-items: flex-start;
  }
  .card-back .brand-name { font-size: 26px; }

  .contact-list {
    position: absolute; left: 44px; top: 122px;
    list-style: none;
    font-size: 13px;
    line-height: 22px;
    color: var(--ink);
  }
  .contact-list li { display: flex; align-items: center; gap: 10px; }
  .contact-icon { width: 14px; height: 14px; flex: none; }

  .person {
    position: absolute; right: 110px; top: 258px; text-align: right;
  }
  .person-name { font-size: 17px; font-weight: 600; color: var(--red); }
  .person-title { font-size: 13px; color: var(--ink); margin-top: 2px; }

  .footer-band { position: absolute; left: 0; bottom: 0; width: 700px; height: 70px; }
  .footer-url {
    position: absolute; right: 34px; bottom: 14px;
    font-size: 13px; letter-spacing: 3px; color: #ffffff;
  }
</style>
</head>
<body>

<section class="card card-front" aria-label="Card front">
  <div class="brand">
    <div class="brand-row">
      <span class="brand-mark"></span>
      <span class="brand-name">KTR Commercial</span>
    </div>
    <span class="brand-tagline">Invest · Build · Manage</span>
  </div>
</section>

<section class="card card-back" aria-label="Card back">
  <div class="brand">
    <div class="brand-row">
      <span class="brand-mark"></span>
      <span class="brand-name">KTR Commercial</span>
    </div>
    <span class="brand-tagline">Invest · Build · Manage</span>
  </div>

  <ul class="contact-list">
    <li>
      <svg class="contact-icon" viewBox="0 0 14 14"><circle cx="7" cy="7" r="7" fill="var(--red)"/><path d="M7 3.2a2.3 2.3 0 0 0-2.3 2.3C4.7 7.3 7 10.6 7 10.6s2.3-3.3 2.3-5.1A2.3 2.3 0 0 0 7 3.2z" fill="#fff"/></svg>
      <span>4780 Brambling Road</span>
    </li>
    <li>
      <svg class="contact-icon" viewBox="0 0 14 14"><circle cx="7" cy="7" r="7" fill="var(--red)"/></svg>
      <span>Suite 610, Atlanta, GA 30342</span>
    </li>
    <li>
      <svg class="contact-icon" viewBox="0 0 14 14"><circle cx="7" cy="7" r="7" fill="var(--red)"/><path d="M4.6 3.8l1.3-.3.8 1.8-.9.7a5 5 0 0 0 2.2 2.2l.7-.9 1.8.8-.3 1.3c-3.2.2-5.8-2.4-5.6-5.6z" fill="#fff"/></svg>
      <span>(404) 555-0142</span>
    </li>
    <li>
      <svg class="contact-icon" viewBox="0 0 14 14"><circle cx="7" cy="7" r="7" fill="var(--red)"/><path d="M4.6 3.8l1.3-.3.8 1.8-.9.7a5 5 0 0 0 2.2 2.2l.7-.9 1.8.8-.3 1.3c-3.2.2-5.8-2.4-5.6-5.6z" fill="#fff"/></svg>
      <span>(404) 555-0187</span>
    </li>
    <li>
      <svg class="contact-icon" viewBox="0 0 14 14"><circle cx="7" cy="7" r="7" fill="var(--red)"/><rect x="3.6" y="4.6" width="6.8" height="4.8" fill="none" stroke="#fff" stroke-width="1"/><path d="M3.6 4.8L7 7.4l3.4-2.6" fill="none" stroke="#fff" stroke-width="1"/></svg>
      <span>dalton@ktrcommercial.net</span>
    </li>
  </ul>

  <div class="person">
    <p class="person-name">H. Dalton Greave</p>
    <p class="person-title">President</p>
  </div>

  <svg class="footer-band" viewBox="0 0 700 70" preserveAspectRatio="none" aria-hidden="true">
    <rect x="0" y="40" width="280" height="30" fill="var(--red)"/>
    <path d="M250 70 C275 70 270 28 300 28 L700 28 L700 70 Z" fill="var(--slate-light)"/>
    <path d="M262 70 C287 70 282 34 312 34 L700 34 L700 70 Z" fill="var(--slate)"/>
  </svg>
  <span class="footer-url">www.ktrcommercial.net</span>
</section>

</body>
</html>
```